Company or website name
- Dr. Renaud Vasquelle
- Links to the website
- Retired doctor; professional speaker, Life coach, author, healthcare consultant
- Other Facts

```html
<!DOCTYPE html>
<html lang="en">
<head>
<meta charset="utf-8">
<title>Dr. Renaud Vasquelle – Professional Speaker, Author &amp; Life Coach</title>
<link rel="stylesheet" href="https://fonts.googleapis.com/css2?family=Varela+Round&family=Alegreya:ital,wght@0,700;1,400&display=swap">
<style>
  :root {
    --backdrop: #cbcbcb;
    --frame: #ffffff;
    --navy: #2e4766;
    --steel-top: #6a8290;
    --steel-bottom: #546b86;
    --steel-edge: #4d6580;
    --steel-foot: #96a6b9;
    --sand: #e0d6c0;
    --band: #3b5577;
    --gold: #f5d36a;
    --lavender-a: #c9cbe6;
    --lavender-b: #b5b9df;
    --ink: #1b1f3a;
    --muted: #8b8a86;
    --sans: "Varela Round", Arial, sans-serif;
    --serif: "Alegreya", Georgia, serif;
  }
  * { box-sizing: border-box; margin: 0; padding: 0; }
  html, body { width: 1108px; height: 1200px; overflow: hidden; background: var(--backdrop); }
  .page {
    position: absolute; left: 88px; top: 41px; width: 933px; height: 1118px;
    background: var(--frame); box-shadow: 0 0 6px rgba(0,0,0,.35);
  }
  .page > * { position: absolute; }
  .brand { left: 4.6px; top: 4.6px; width: 277px; height: 184.7px; background: var(--navy); color: #fff; font-family: var(--sans); }
  .brand-name { position: absolute; left: 23px; top: 56px; font-size: 33px; line-height: 30px; letter-spacing: -0.5px; }
  .brand-role { position: absolute; left: 23px; top: 131px; font-size: 11.5px; font-style: italic; }
  .sidebar {
    left: 4.6px; top: 189.3px; width: 277px; height: 826.5px;
    background: linear-gradient(var(--steel-top), var(--steel-bottom));
    border-bottom: 28px solid var(--steel-edge);
  }
  .sidebar ul { list-style: none; padding: 23px 0 0 28px; }
  .sidebar li { font-family: var(--sans); font-size: 18.5px; line-height: 32.7px; }
  .sidebar a { color: #fff; text-decoration: none; }
  .sidebar a.current { color: var(--gold); }
  .sidebar-foot { left: 4.6px; top: 1020.5px; width: 277px; height: 92.3px; background: var(--steel-foot); }
  .masthead { left: 286px; top: 4.6px; width: 642px; height: 87.7px; background: var(--sand); }
  .band-left { position: absolute; left: 0; top: 19px; width: 379px; height: 11px; background: var(--band); }
  .band-right { position: absolute; right: 0; top: 19px; width: 21px; height: 11px; background: var(--band); }
  .top-nav { position: absolute; left: 396px; top: 15px; display: flex; gap: 16px; font-family: var(--sans); font-size: 15.5px; -webkit-text-stroke: 0.3px var(--band); }
  .top-nav a { color: var(--band); text-decoration: none; }
  .tagline { position: absolute; left: 11px; top: 60px; font-family: var(--serif); font-style: italic; font-size: 19px; color: var(--muted); }
  .hero {
    left: 286px; top: 97px; width: 642px; height: 461.6px;
    background: linear-gradient(180deg, #c9cdd2 0%, #8ea3c1 40%, #6d7a8c 62%, #3f3a36 100%);
  }
  .purpose { left: 286px; top: 563.3px; width: 642px; height: 184.7px; background: linear-gradient(90deg, var(--lavender-a), var(--lavender-b)); }
  .portrait { position: absolute; left: 0; top: 0; width: 138.5px; height: 184.7px; background: radial-gradient(circle at 50% 40%, #8f93d6, #3a3f8a); }
  .purpose-text { position: absolute; left: 157px; top: 13px; width: 475px; font-family: var(--serif); color: var(--ink); }
  .purpose-text h2 { font-size: 20px; font-weight: 700; margin-bottom: 6px; }
  .purpose-text p { font-style: italic; font-size: 18.6px; line-height: 21.5px; margin-bottom: 10px; }
  .intro {
    left: 286px; top: 802px; width: 642px; text-align: center;
    font-family: var(--sans); font-size: 17.6px; line-height: 25.8px; color: var(--ink);
    -webkit-text-stroke: 0.45px var(--ink);
  }
  .footer { left: 286px; top: 1020.5px; width: 642px; height: 92.3px; background: var(--sand); font-family: var(--sans); color: #4a4a4a; }
  .footer .copy { position: absolute; left: 18px; top: 31px; font-size: 14.8px; }
  .footer .copy strong { color: #33333f; }
  .footer .note { position: absolute; left: 18px; top: 51px; font-size: 12px; }
</style>
</head>
<body>
<div class="page">
  <header class="brand">
    <div class="brand-name">RENAUD<br>VASQUELLE</div>
    <div class="brand-role">Professional Speaker, Author &amp; Life Coach</div>
  </header>
  <nav class="sidebar">
    <ul>
      <li><a class="current" href="#">The 60-Second Lift</a></li>
      <li><a href="#">Words of Wisdom</a></li>
      <li><a href="#">Available Seminar Topics</a></li>
      <li><a href="#">Plain Wisdom Series</a></li>
      <li><a href="#">Videos</a></li>
      <li><a href="#">Building Your Bright Life</a></li>
      <li><a href="#">About Your Speaker</a></li>
      <li><a href="#">Want Coaching?</a></li>
      <li><a href="#">Booking Renaud</a></li>
      <li><a href="#">Contact Us</a></li>
    </ul>
  </nav>
  <div class="sidebar-foot"></div>
  <div class="masthead">
    <div class="band-left"></div>
    <nav class="top-nav"><a href="#">HOME</a><a href="#">ABOUT</a><a href="#">CONTACT</a></nav>
    <div class="band-right"></div>
    <p class="tagline">★ Bring fresh eyes to everyday things.</p>
  </div>
  <div class="hero" role="img" aria-label="Photo of a person sitting on a boulder looking toward a snowy mountain range under a cloudy sky"></div>
  <section class="purpose">
    <div class="portrait" role="img" aria-label="Portrait photo of the speaker in a vest and striped tie"></div>
    <div class="purpose-text">
      <h2>My Purpose Statement:</h2>
      <p>“I hereby pledge my life to my greatest expression of love and service for the benefit of all humanity.</p>
      <p>I accomplish this by helping people tap into their potential, using the written and spoken word; empowering ordinary people into exceptional life-fulfilled individuals.”</p>
    </div>
  </section>
  <p class="intro">The information found on this website<br>is intended to inspire you to achieve your full potential.<br>There are a variety of resources including<br>the 60-Second Lift,<br>the Plain Wisdom Series,<br>Building Your Bright Life,<br>and many other great resources<br>to help make every day a terrific day!</p>
  <footer class="footer">
    <p class="copy">Copyright © 2012, <strong>Dr. Renaud Vasquelle</strong>. All Rights Reserved.</p>
    <p class="note">Comments, questions or suggestions can be directed to webmaster@renaudvasquelle.com.</p>
  </footer>
</div>
</body>
</html>
```